Velmora Group
Velmora Financial
Velmora Group -
Creative Brief
Pirot Brekon
Partner
318 Elmwick Lane London E9 4PQ United Kingdom
Pbrekon@quillmesh.net
Company No. 5281947
Please provide an alternative design with the name Velmora Group instead of Velmora Financial
Just the logo

```html
<!DOCTYPE html>
<html lang="en">
<head>
<meta charset="utf-8">
<title>Velmora Group – Logo Presentation</title>
<link rel="stylesheet" href="https://fonts.googleapis.com/css2?family=Libre+Caslon+Text:wght@400;700&display=swap">
<style>
  :root {
    --page: #ffffff;
    --navy: #16438c;
    --blue: #1f6fc4;
    --sky: #35a3e6;
    --ink: #3a3a3a;
    --black: #0b0b0b;
    --silver: #d4d4d4;
    --white: #ffffff;
    --muted: #777777;
    --rule: #cfcfcf;
    --serif: "Libre Caslon Text", Georgia, serif;
  }
  * { margin: 0; padding: 0; box-sizing: border-box; }
  html, body { width: 1200px; height: 706px; overflow: hidden; background: var(--page); }
  .sheet { position: relative; width: 1200px; height: 706px; font-family: var(--serif); }

  .card { position: absolute; width: 557px; height: 306px; overflow: hidden; }
  .card--front { left: 26px; top: 34px; background: var(--white); box-shadow: 0 0 0 1px var(--rule); }
  .card--blue  { left: 617px; top: 34px; background: linear-gradient(100deg, var(--navy) 0%, var(--blue) 55%, var(--sky) 100%); }
  .card--mono  { left: 26px; top: 368px; background: linear-gradient(100deg, var(--black) 0%, #3c3c3c 45%, var(--silver) 100%); }
  .card--light { left: 617px; top: 368px; background: var(--white); box-shadow: 0 0 0 1px var(--rule); }

  .band { position: absolute; inset: 0; width: 100%; height: 100%; }

  /* Logo lockup: plain square above the name */
  .brand { position: absolute; display: flex; flex-direction: column; align-items: center; }
  .brand__mark { width: 34px; height: 34px; background: currentColor; margin-bottom: 18px; }
  .brand__name { font-weight: 700; letter-spacing: 0.06em; text-transform: uppercase; white-space: nowrap; line-height: 1; }
  .brand__tag { letter-spacing: 0.42em; text-transform: uppercase; font-weight: 400; white-space: nowrap; margin-top: 7px; }

  .card--front .brand { left: 36px; top: 36px; width: 230px; color: var(--navy); }
  .card--front .brand__mark { width: 22px; height: 22px; margin-bottom: 12px; }
  .card--front .brand__name { font-size: 22px; color: var(--ink); }
  .card--front .brand__tag { font-size: 6.5px; margin-top: 5px; color: var(--ink); }

  .card--blue .brand, .card--mono .brand, .card--light .brand { left: 0; right: 0; top: 118px; }
  .card--blue .brand, .card--mono .brand { color: var(--white); }
  .card--light .brand { color: var(--ink); }
  .card--light .brand__mark { color: var(--blue); }
  .card--blue .brand__name, .card--mono .brand__name, .card--light .brand__name { font-size: 34px; }
  .card--blue .brand__tag, .card--mono .brand__tag, .card--light .brand__tag { font-size: 9.5px; }

  .person { position: absolute; left: 385px; top: 66px; }
  .person__name { font-size: 22px; color: var(--blue); line-height: 1.1; }
  .person__role { font-size: 10px; color: var(--muted); margin-top: 3px; text-align: right; }

  .contact { position: absolute; left: 22px; bottom: 18px; color: var(--white); font-size: 11.5px; line-height: 1.45; font-style: normal; }
</style>
</head>
<body>
<main class="sheet">

  <section class="card card--front">
    <svg class="band" viewBox="0 0 557 306" preserveAspectRatio="none" aria-hidden="true">
      <defs>
        <linearGradient id="bandFill" x1="0" y1="0" x2="1" y2="0">
          <stop offset="0" stop-color="#16438c"/>
          <stop offset="0.6" stop-color="#1f6fc4"/>
          <stop offset="1" stop-color="#35a3e6"/>
        </linearGradient>
      </defs>
      <polygon points="0,170 557,210 557,306 0,306" fill="#35a3e6" opacity="0.5"/>
      <polygon points="0,180 557,226 557,306 0,306" fill="url(#bandFill)"/>
    </svg>
    <div class="brand">
      <span class="brand__mark"></span>
      <span class="brand__name">Velmora Group</span>
      <span class="brand__tag">Engineering Solutions</span>
    </div>
    <div class="person">
      <div class="person__name">Pirot Brekon</div>
      <div class="person__role">Partner</div>
    </div>
    <address class="contact">
      318 Elmwick Lane, London E9 4PQ, United Kingdom<br>
      Phone: +44(0)7700900412 | Cell: +44(0)2079460318<br>
      Email: Pbrekon@quillmesh.net | License No.: Company No. 5281947
    </address>
  </section>

  <section class="card card--blue">
    <div class="brand">
      <span class="brand__mark"></span>
      <span class="brand__name">Velmora Group</span>
      <span class="brand__tag">Engineering Solutions</span>
    </div>
  </section>

  <section class="card card--mono">
    <div class="brand">
      <span class="brand__mark"></span>
      <span class="brand__name">Velmora Group</span>
      <span class="brand__tag">Engineering Solutions</span>
    </div>
  </section>

  <section class="card card--light">
    <div class="brand">
      <span class="brand__mark"></span>
      <span class="brand__name">Velmora Group</span>
      <span class="brand__tag">Engineering Solutions</span>
    </div>
  </section>

</main>
</body>
</html>
```